Flyer Design Project

We need a single sided flyer designed to insert in to DL size envelopes promoting our products & services.

what we do can be seen at www.brightleafstaging.com.au

Must incorporate our logo, website and telephone number (1300 587 690)

The Byline "Conferences - Events - Meetings - Expo Rental - Venue Services - Awards Nights - IT Rental - Recording - Gala Dinners"

No other text is required

Flyer needs to have a relevant background design either geometric or related to our products & services

The design needs to portray us with corporate professionalism and adhere to our existing colour scheme however use less white than our website.

Target Market(s)

Hotels, conference organisers, venues

Industry/Entity Type

Events

Requirements
Must have
• Must incorporate our logo, website and telephone number

Must have a designed image or shape in the background
Should not have
• play, pause, or stop symbols
cogs or gears
stock photos of data projectors

```html
<!DOCTYPE html>
<html lang="en">
<head>
<meta charset="utf-8">
<title>Brightleaf Staging – DL Flyer</title>
<link rel="stylesheet" href="https://fonts.googleapis.com/css2?family=Barlow:wght@300;400;600&display=swap">
<style>
  :root {
    --ink: #0d0d0d;
    --paper: #ffffff;
    --brand-blue: #1b5ea4;
    --brand-red: #e8372a;
    --crowd-dark: #111111;
    --crowd-light: #d9d9d9;
  }
  * { margin: 0; padding: 0; box-sizing: border-box; }
  html, body {
    width: 1200px;
    height: 567px;
    overflow: hidden;
    background: var(--paper);
  }
  .flyer {
    position: relative;
    width: 1200px;
    height: 567px;
    overflow: hidden;
    font-family: "Barlow", "Helvetica Neue", Arial, sans-serif;
  }
  .crowd-artwork {
    position: absolute;
    inset: 0;
    background:
      linear-gradient(100deg, var(--crowd-dark) 0%, #3a3a3a 22%, var(--crowd-light) 40%, #2b2b2b 62%, #6e6e6e 78%, var(--crowd-dark) 100%);
  }
  .info-panel {
    position: absolute;
    left: 204px;
    top: 0;
    width: 361px;
    height: 428px;
    background: var(--paper);
  }
  .brand {
    position: absolute;
    left: 24px;
    top: 44px;
    display: flex;
    align-items: center;
    gap: 12px;
  }
  .brand-mark {
    width: 40px;
    height: 40px;
    background: var(--brand-blue);
  }
  .brand-name {
    font-weight: 600;
    font-size: 31px;
    line-height: 1;
    color: var(--brand-blue);
    letter-spacing: -0.2px;
  }
  .services {
    position: absolute;
    left: 33px;
    top: 144px;
    list-style: none;
  }
  .services li {
    font-weight: 400;
    font-size: 22px;
    line-height: 29px;
    color: var(--brand-blue);
    letter-spacing: 0.3px;
  }
  .contact-band {
    position: absolute;
    left: 204px;
    top: 475px;
    width: 361px;
    height: 92px;
    background: var(--brand-red);
    color: var(--paper);
    text-align: center;
    font-weight: 300;
  }
  .contact-web {
    position: absolute;
    left: 0;
    right: 0;
    top: 12px;
    font-size: 18.5px;
    letter-spacing: 0.2px;
  }
  .contact-phone {
    position: absolute;
    left: 0;
    right: 0;
    top: 47px;
    font-size: 21px;
    letter-spacing: 0.6px;
  }
</style>
</head>
<body>
  <main class="flyer">
    <div class="crowd-artwork" role="img" aria-label="High-contrast black and white illustration of a conference audience filling the background"></div>

    <section class="info-panel">
      <div class="brand">
        <span class="brand-mark" aria-hidden="true"></span>
        <span class="brand-name">Brightleaf Staging</span>
      </div>
      <ul class="services">
        <li>Conferences</li>
        <li>Events</li>
        <li>Meetings</li>
        <li>Expo Rental</li>
        <li>Venue Services</li>
        <li>Awards Nights</li>
        <li>IT Rental</li>
        <li>Recording</li>
        <li>Gala Dinners</li>
      </ul>
    </section>

    <footer class="contact-band">
      <p class="contact-web">www.brightleafstaging.com.au</p>
      <p class="contact-phone">1300 587 690</p>
    </footer>
  </main>
</body>
</html>
```